Project Manager Business Card for Top Architectural Firm

Update and design a stunning Senior Project Manager Business Card

MARCO T. DRUMMOND II
Senior Project Manager

H A L C Y O N
A R C H I T E C T U R E L L C.
www.HalcyonGrandEstates.example
4127 NW 52nd Ter. Suite 2308
Miami, FL 33148
C: (305) 555-0184
mdrummond.halcyongrandestates@mailbox.example

Looking to have the logo to be UV Spot ink printed and to be prominent.

Target Market(s)

High end real estate architecture construction

Industry/Entity Type

Architect

Contact Information for Business Card

MARCO T. DRUMMOND II
Senior Project Manager

H A L C Y O N
Miami, FL 33148
C: (305) 555-0184

Font styles to use
Sans Serif

Colors

Designer to choose colors to be used in the design.

Requirements
Must have
• Prominent Logo

```html
<!DOCTYPE html>
<html lang="en">
<head>
<meta charset="utf-8">
<title>Halcyon Architecture – Business Card</title>
<link rel="stylesheet" href="https://fonts.googleapis.com/css2?family=Arimo:wght@400;700&display=swap">
<style>
  :root {
    --backdrop: #2b2b2d;
    --card: #1b1b1d;
    --card-edge: #111113;
    --accent: #2fa8e6;
    --text: #f2f2f2;
    --text-soft: #d9d9d9;
    --mark-back: #3a3a3e;
    --divider: #e6e6e6;
  }
  html, body {
    margin: 0;
    width: 1200px;
    height: 954px;
    overflow: hidden;
    background: var(--backdrop);
    font-family: "Arimo", Arial, sans-serif;
  }
  .canvas {
    position: relative;
    width: 1200px;
    height: 954px;
  }
  .card {
    position: absolute;
    left: 285px;
    width: 630px;
    height: 360px;
    background: var(--card);
    border-radius: 4px;
    box-shadow: 0 6px 0 var(--card-edge), 0 18px 30px rgba(0,0,0,.45);
    overflow: hidden;
  }
  .card--back { top: 82px; }
  .card--front { top: 512px; }
  .accent-line {
    position: absolute;
    left: 0;
    right: 0;
    top: 282px;
    height: 3px;
    background: var(--accent);
  }

  /* wordmark: one colour, one weight */
  .wordmark {
    position: absolute;
    text-align: center;
    font-weight: 400;
    white-space: nowrap;
  }
  .wordmark__dot {
    display: block;
    margin: 0 auto 14px;
    border-radius: 50%;
  }
  .wordmark__name {
    display: block;
    letter-spacing: 0.32em;
    margin-right: -0.32em;
  }
  .wordmark__sub {
    display: block;
    letter-spacing: 0.28em;
    margin-right: -0.28em;
    margin-top: 4px;
  }

  .card--back .wordmark {
    left: 0; right: 0; top: 56px;
    color: var(--mark-back);
  }
  .card--back .wordmark__dot {
    width: 82px; height: 82px;
    background: var(--mark-back);
  }
  .card--back .wordmark__name { font-size: 40px; }
  .card--back .wordmark__sub { font-size: 9px; }

  .card--front .wordmark {
    left: 24px; width: 206px; top: 66px;
    color: var(--text);
  }
  .card--front .wordmark__dot {
    width: 84px; height: 84px;
    background: var(--accent);
  }
  .card--front .wordmark__name {
    font-size: 27px;
    letter-spacing: 0.2em;
    margin-right: -0.2em;
  }
  .card--front .wordmark__sub {
    font-size: 7.5px;
    letter-spacing: 0.24em;
    margin-right: -0.24em;
  }

  .divider {
    position: absolute;
    left: 250px;
    top: 60px;
    width: 2px;
    height: 168px;
    background: var(--divider);
  }
  .details {
    position: absolute;
    left: 268px;
    top: 62px;
    right: 14px;
    color: var(--text);
  }
  .details__name {
    margin: 0;
    font-size: 19px;
    font-weight: 700;
    letter-spacing: 0.02em;
  }
  .details__role {
    margin: 3px 0 0;
    font-size: 8.5px;
    font-weight: 700;
    letter-spacing: 0.18em;
    color: var(--accent);
    text-transform: uppercase;
  }
  .details__address {
    margin: 26px 0 0;
    font-style: normal;
    font-size: 15px;
    line-height: 21px;
    color: var(--text-soft);
  }
  .contact {
    list-style: none;
    margin: 24px 0 0;
    padding: 0;
  }
  .contact__item {
    display: flex;
    align-items: center;
    gap: 7px;
    font-size: 14px;
    line-height: 20px;
    color: var(--text-soft);
    white-space: nowrap;
  }
  .contact__item--small { font-size: 12.6px; }
  .contact__icon {
    width: 14px;
    height: 14px;
    flex: none;
    fill: none;
    stroke: var(--accent);
    stroke-width: 1.6;
  }
</style>
</head>
<body>
<main class="canvas">

  <section class="card card--back" aria-label="Card back">
    <div class="wordmark">
      <span class="wordmark__dot"></span>
      <span class="wordmark__name">HALCYON</span>
      <span class="wordmark__sub">ARCHITECTURE LLC.</span>
    </div>
    <div class="accent-line"></div>
  </section>

  <section class="card card--front" aria-label="Card front">
    <div class="wordmark">
      <span class="wordmark__dot"></span>
      <span class="wordmark__name">HALCYON</span>
      <span class="wordmark__sub">ARCHITECTURE LLC.</span>
    </div>

    <div class="divider"></div>

    <div class="details">
      <h1 class="details__name">MARCO T. DRUMMOND II</h1>
      <p class="details__role">Senior Project Manager</p>
      <address class="details__address">
        4127 NW 52nd Ter. Suite 2308<br>
        Miami, FL 33148
      </address>
      <ul class="contact">
        <li class="contact__item">
          <svg class="contact__icon" viewBox="0 0 16 16" aria-hidden="true">
            <path d="M3 2.5l3 .5 1 3-1.6 1.2a8 8 0 0 0 3.4 3.4L10 9l3 1 .5 3c-5.5.8-11.3-5-10.5-10.5z"/>
          </svg>
          <span>(305) 555-0184</span>
        </li>
        <li class="contact__item contact__item--small">
          <svg class="contact__icon" viewBox="0 0 16 16" aria-hidden="true">
            <rect x="1.5" y="3.5" width="13" height="9" rx="1"/>
            <path d="M1.5 4l6.5 5 6.5-5"/>
          </svg>
          <span>mdrummond.halcyongrandestates@mailbox.example</span>
        </li>
        <li class="contact__item">
          <svg class="contact__icon" viewBox="0 0 16 16" aria-hidden="true">
            <circle cx="8" cy="8" r="6.2"/>
            <ellipse cx="8" cy="8" rx="2.8" ry="6.2"/>
            <path d="M1.8 8h12.4M3 4.8h10M3 11.2h10"/>
          </svg>
          <span>www.HalcyonGrandEstates.example</span>
        </li>
      </ul>
    </div>

    <div class="accent-line"></div>
  </section>

</main>
</body>
</html>
```